Human Resource Consulting practice needs a business card design

We need a business card design (double sided colour) for our Human Resource (HR) consulting practice in regional New South Wales, australia. Our business name is Staffwise Partners. We support small and medium business across the Mid North Coast of New South Wales by providing them with outsourced HR support, services and products to help them achieve compliance with workplace legislation and across all areas of the employment lifecycle from recruitment to termination and everything in between. Our corporate colours are hot pink and black. The final design should communicate professionalism, trust, people focus.
I have attached the current (old) business card for your reference.

Target Market(s)

Business owners and high level managers

Industry/Entity Type

Business

Contact Information for Business Card

Name
Title
Phone no
Mobile no
Address
PO Box
email address
website

Colors
e34197

Requirements
Must have
• Tempate for changing business card personal details including Name, position title, mobile number, email address.
• Keep current logo and colours as per attached
• Logo must be presented in 2 colours or black only not white
Nice to have
• One side logo and graphic only other side logo and personal details
Should not have
• Should not be the same as the current version (attached) but a modern interpretation.
• Does not need a busy reverse side with our list of services as per current version. I feel this is too busy.
• No photos

```html
<!DOCTYPE html>
<html lang="en">
<head>
<meta charset="utf-8">
<title>Staffwise Partners — Business Card</title>
<link href="https://fonts.googleapis.com/css2?family=Michroma&display=swap" rel="stylesheet">
<style>
  :root {
    --hot-pink: #e80e8f;
    --ink: #1d1b1c;
    --paper: #ffffff;
    --backdrop: #e9e7e8;
    --rule: #3a3a3a;
    --font-main: "Michroma", sans-serif;
  }
  * { box-sizing: border-box; margin: 0; padding: 0; }
  html, body {
    width: 1200px; height: 1189px; overflow: hidden;
    background: var(--backdrop);
    font-family: var(--font-main);
  }
  .canvas { position: relative; width: 1200px; height: 1189px; }
  .card {
    position: absolute; left: 220px; width: 760px; height: 464px;
    border-radius: 26px;
    box-shadow: 0 10px 30px rgba(0,0,0,.18);
  }

  /* Front: brand side */
  .card--front { top: 80px; background: var(--hot-pink); }
  .card--front .brand {
    position: absolute; left: 0; right: 0; top: 160px;
    display: flex; justify-content: center; align-items: center;
  }
  .brand__name {
    font-size: 40px; color: var(--ink); letter-spacing: 1px; white-space: nowrap;
  }
  .front__web {
    position: absolute; left: 70px; right: 70px; top: 300px;
    display: flex; align-items: center; gap: 18px;
    font-size: 14px; color: var(--ink); letter-spacing: 1px;
  }
  .front__web::before, .front__web::after {
    content: ""; flex: 1; height: 1px; background: var(--ink);
  }

  /* Back: details side */
  .card--back { top: 630px; background: var(--paper); }
  .card--back .brand {
    position: absolute; left: 54px; top: 58px;
    display: flex; align-items: center;
  }
  .card--back .brand__name { font-size: 30px; }
  .person { position: absolute; right: 48px; top: 150px; text-align: right; }
  .person__name { font-size: 26px; color: var(--hot-pink); font-weight: 400; letter-spacing: 1px; }
  .person__title { font-size: 13px; color: var(--ink); letter-spacing: 1px; margin-top: 6px; }
  .divider {
    position: absolute; left: 54px; right: 48px; top: 222px;
    height: 1px; background: var(--rule);
  }
  .contacts {
    position: absolute; left: 54px; top: 252px; list-style: none;
  }
  .contacts li {
    display: flex; align-items: center; gap: 16px;
    font-size: 16px; color: var(--ink); letter-spacing: 1px;
    height: 38px;
  }
  .contacts svg { width: 26px; height: 26px; flex: none; }
  .address {
    position: absolute; right: 48px; top: 262px; text-align: right;
    font-size: 16px; line-height: 30px; color: var(--ink); letter-spacing: 1px;
    font-style: normal;
  }
</style>
</head>
<body>
<main class="canvas">

  <section class="card card--front" aria-label="Card front">
    <div class="brand">
      <span class="brand__name">Staffwise Partners</span>
    </div>
    <p class="front__web">www.staffwisepartners.com.au</p>
  </section>

  <section class="card card--back" aria-label="Card back">
    <div class="brand">
      <span class="brand__name">Staffwise Partners</span>
    </div>

    <div class="person">
      <h1 class="person__name">Dana Whitlock</h1>
      <p class="person__title">PRINCIPAL CONSULTANT</p>
    </div>

    <div class="divider"></div>

    <ul class="contacts">
      <li>
        <svg viewBox="0 0 26 26" aria-hidden="true"><rect width="26" height="26" rx="5" fill="var(--hot-pink)"/><path d="M7 9c0-2 3-3 6-3s6 1 6 3v2h-3V9.5h-6V11H7z M8 12h10l1 7H7z" fill="#fff"/></svg>
        02 6500 1248
      </li>
      <li>
        <svg viewBox="0 0 26 26" aria-hidden="true"><rect width="26" height="26" rx="5" fill="var(--hot-pink)"/><rect x="9" y="5" width="8" height="16" rx="1.5" fill="#fff"/><rect x="10.5" y="7" width="5" height="6" fill="var(--hot-pink)"/></svg>
        0400 372 915
      </li>
      <li>
        <svg viewBox="0 0 26 26" aria-hidden="true"><rect width="26" height="26" rx="5" fill="var(--hot-pink)"/><rect x="5" y="8" width="16" height="11" fill="#fff"/><path d="M5 8l8 6 8-6" fill="none" stroke="var(--hot-pink)" stroke-width="1.5"/></svg>
        dana@staffwisepartners.com.au
      </li>
      <li>
        <svg viewBox="0 0 26 26" aria-hidden="true"><rect width="26" height="26" rx="5" fill="var(--hot-pink)"/><circle cx="13" cy="13" r="7.5" fill="none" stroke="#fff" stroke-width="1.6"/><ellipse cx="13" cy="13" rx="3" ry="7.5" fill="none" stroke="#fff" stroke-width="1.2"/><path d="M5.5 13h15" stroke="#fff" stroke-width="1.2"/></svg>
        www.staffwisepartners.com.au
      </li>
    </ul>

    <address class="address">
      P.O. Box 210<br>Harbour Bay, NSW 2400
    </address>
  </section>

</main>
</body>
</html>
```